Vacation/Holiday Home Wordpress Website

I currently have a website for our vacation/holiday rental home. It is 6 years old and needs a complete redesign to acommodate many new features available today. The existing website can be seen at www.coralwindstays.co.uk . The purpose of the website is mainly to provide useful infomation about our home, the destination of Barbados. The customer is also able to check availability and book. Please note that there is a booking element to the website which is hosted externally. This can be seen at

http://stay.reservequick-hub.net/PickArrival_Mini.asp?ref=kTR%3DWQPA%26LMN%3DHXJX

I now wish to add key functionality such as:

- Video of property and area
- Customer video testimonials
- Other useful information

The navigation, menus and buttons need to be re designed to give a modern, innovative and professional look and feel.

My customers are mainly females between the ages of 35 and 55. The website needs to reassure customers who are parting with a lot of mony by booking online. It needs to give a sense of trust as this may be a once in a lifetime trip which they have saved up for for a long time. Many visitors to the website will be referred by other websites such as www.nestroam.co.uk and www.villaquarters.co.uk.
Updates

Dear designers, 

Thank you for taking the time to write some further comments to you all. 

1. The homepage should have an availability search function as a key feature

2. The look and feel does NOT need to have the 3 feature columns like my current website has

3.  There should not be too much text on the homepage. Brief text can be included with 'more'  buttons to reveal more information 

4.  For designs that are under consideration, we will need to see a design for the other pages as they will be different to the homepage. Information from other pages on the existing website can be used. 

Reason: Dear all, I will be providing extensive feedback later today following a review that we have conducted with a group of our guests. To enable you to read and use this information, we have extended the deadline by 5 days. Thank you for the design submisions so far. We hope that the additional feedback will enable you to amend your designs appropriately. Regards Martin Elswick

Dear all,

Thank you for your designs.  I apologise that I am unable to give detailed feedback on each and every design submitted.  I will contact you individually and indicate whether we would like you to submit any further designs.  These should take into account the feedback below.

Feedback from design review group

1.  Logo should not be displayed in a white box.  It should blend in with the background or be overlayed onto the picture.

2.  There must be an availability calendar on the home page.

3.  Any background image should be subtle, maybe blurred and not distract from the main area.

4.  Text should be limited to a few key words with a 'read more' button to reveal more information.

5.  A gallery/slide show should be featured in the top part of the screen

6.  Icons can be used as navigation buttons

7.  Video testimonials is a key feature and should appear on the home page

8.   The use of bold and vibrant colours is preferred

9.   The 3 column format of the old website should not be copied

Regards

Martin

Target Market(s)

Female's, Families, 35 to 55 year olds, travellers to Barbados

Industry/Entity Type

Online

Requirements
Must have
• Pictures
Video
Testimonials
Clear and stylish navigation
Easy to use navigation
Should not have
• Dated look or feel

```html
<!DOCTYPE html>
<html lang="en">
<head>
<meta charset="utf-8">
<title>Coral Wind Stays</title>
<link href="https://fonts.googleapis.com/css2?family=Nunito+Sans:wght@400;600;700&display=swap" rel="stylesheet">
<style>
:root{
  --yellow:#f6c719;
  --yellow-deep:#eeab0a;
  --orange-text:#f0a500;
  --red:#e8242a;
  --green:#5cbb1f;
  --blue:#4fb9ef;
  --white:#ffffff;
  --ink:#2a2820;
  --link:#2a6fd6;
}
*{box-sizing:border-box;margin:0;padding:0}
html,body{width:682px;height:1200px;overflow:hidden;background:var(--white)}
body{position:relative;font-family:"Nunito Sans",Arial,sans-serif}
.abs{position:absolute}

/* hero */
.hero{left:0;top:0;width:682px;height:288px;border-top:3px solid var(--yellow);border-bottom:7px solid var(--yellow);
  background:linear-gradient(180deg,#2f78d6 0%,#6fa9e8 35%,#c9e3ef 55%,#5cc9cf 68%,#e6dfcf 82%,#efe9dc 100%)}
.hero-photo{inset:0}
.brand{left:62px;top:30px;color:var(--white);font-weight:700;font-size:14px;letter-spacing:2px;display:flex;align-items:center;gap:8px}
.brand-dot{width:14px;height:14px;border-radius:50%;background:var(--white)}
.nav{top:29px;left:307px;display:flex;gap:7px}
.nav a{display:block;background:var(--white);color:var(--orange-text);text-decoration:none;font-size:10px;font-weight:700;height:23px;line-height:23px;border-radius:12px;padding:0 12px}
.social{top:28px;left:555px;display:flex;gap:7px}
.social span{width:24px;height:24px;border-radius:50%;background:var(--white);opacity:.9}
.search{left:57px;top:79px;width:161px;height:159px;background:rgba(255,255,255,.72)}
.search .pill{position:absolute;left:9px;top:12px;width:141px;height:19px;border-radius:10px;background:var(--yellow);color:var(--white);font-size:9px;font-weight:700;text-align:center;line-height:19px}
.search .label{position:absolute;left:8px;font-size:10px;color:var(--orange-text);font-weight:600}
.field{position:absolute;height:15px;background:var(--white);font-size:10px;color:#333;line-height:15px;padding-left:6px}
.field i{position:absolute;right:0;top:1px;width:13px;height:13px;background:var(--yellow)}
.field i::after{content:"";position:absolute;left:3px;top:3px;width:5px;height:5px;border-right:1.5px solid #fff;border-bottom:1.5px solid #fff;transform:rotate(45deg)}
.search .go{position:absolute;left:43px;top:131px;width:73px;height:19px;border-radius:10px;background:linear-gradient(#f8d436,#e3a80a);color:var(--white);font-size:10px;text-align:center;line-height:19px}
.headline{left:236px;top:88px;color:var(--white);font-size:21px;line-height:27px;font-weight:600;letter-spacing:.3px}

/* feature cards */
.card{top:323px;width:122px;height:185px;border-radius:16px;overflow:hidden}
.card .icon{position:absolute;left:0;top:10px;width:100%;height:50px;display:flex;justify-content:center}
.card .photo{position:absolute;left:0;top:82px;width:100%;height:79px;border-top:3px solid var(--white);z-index:1}
.card .tag{position:absolute;left:12px;top:71px;width:98px;height:18px;background:var(--white);font-size:8.5px;font-weight:700;text-align:center;line-height:18px;z-index:2}
.card .more{position:absolute;left:15px;top:152px;width:92px;height:18px;border-radius:9px;color:var(--white);font-size:10px;text-align:center;line-height:18px;z-index:2}
.card.home{left:56px;background:var(--red)} .card.home .tag{color:var(--red)}
.card.area{left:210px;background:var(--green)} .card.area .tag{color:var(--green)}
.card.reviews{left:365px;background:var(--yellow)} .card.reviews .tag{color:var(--orange-text)}
.card.sights{left:518px;background:var(--blue)} .card.sights .tag{color:var(--blue)}

/* section headers */
.sec-head{left:58px;width:582px;height:24px;display:flex;align-items:center}
.sec-head .pill{margin-left:12px;height:20px;border-radius:10px;padding:0 14px;font-size:9px;font-weight:700;line-height:20px}
.sec-head .rule{flex:1;height:1px;margin-left:12px}

/* videos */
.videos{left:0;top:551px;width:682px;height:305px;background:linear-gradient(180deg,var(--yellow) 0%,var(--yellow-deep) 100%)}
.videos .pill{background:var(--white);color:var(--orange-text)}
.videos .rule{background:rgba(255,255,255,.7)}
.main-video{left:58px;top:54px;width:355px;height:219px;background:linear-gradient(180deg,#2e79d4 0%,#86bde9 40%,#5fd1d2 60%,#e4dccb 80%,#d8ceb9 100%)}
.play{left:186px;top:70px;width:84px;height:84px;border-radius:50%;background:rgba(40,38,30,.88)}
.play::after{content:"";position:absolute;left:33px;top:23px;border-left:30px solid var(--white);border-top:19px solid transparent;border-bottom:19px solid transparent}
.clip{left:414px;width:226px;height:76px;padding:4px 10px}
.clip.active{background:var(--white)}
.clip .thumb{position:absolute;left:10px;top:4px;width:104px;height:66px;background:linear-gradient(180deg,#3480d6,#9cc9ea 50%,#5ccad1 65%,#e7e0cf 85%)}
.clip p{position:absolute;left:122px;top:4px;width:100px;font-size:8.5px;line-height:12.4px;color:var(--white)}
.clip.active p{color:var(--link)}
.clip b{font-weight:700}

/* gallery */
.gallery .pill{background:var(--yellow);color:var(--white)}
.gallery .rule{background:var(--yellow)}
.shot{width:90px;height:89px;border:1px solid #ddd}
.shot.beach{background:linear-gradient(180deg,#2f7ad5 0%,#9ccbea 48%,#56c9d2 62%,#ece6d6 80%)}
.shot.villa{background:linear-gradient(180deg,#5c9be0 0%,#a9cdef 30%,#e2cfa4 55%,#cdb58a 75%,#7b8a5a 100%)}

/* footer */
.footer{left:0;top:1144px;width:682px;height:56px;background:var(--ink);color:var(--white);font-size:7.2px;line-height:10px;padding:16px 56px 0}
</style>
</head>
<body>

<header class="abs hero">
  <div class="abs hero-photo" role="img" aria-label="Soft blurred photo of a tropical beach with palm trees and turquoise sea"></div>
  <div class="abs brand"><span class="brand-dot"></span>CORAL WIND STAYS</div>
  <nav class="abs nav"><a href="#">THE HOME</a><a href="#">BOOKING</a><a href="#">CONTACT US</a></nav>
  <div class="abs social"><span></span><span></span><span></span></div>

  <form class="abs search">
    <div class="pill">AVAILABILITY SEARCH</div>
    <div class="label" style="top:37px">ARRIVAL DATE</div>
    <div class="field" style="left:8px;top:55px;width:37px">16<i></i></div>
    <div class="field" style="left:52px;top:55px;width:45px">AUG<i></i></div>
    <div class="field" style="left:106px;top:55px;width:46px">2013<i></i></div>
    <div class="label" style="top:80px">LENGTH OF STAY</div>
    <div class="field" style="left:8px;top:101px;width:37px">8<i></i></div>
    <div class="label" style="left:50px;top:101px">NIGHTS</div>
    <div class="go">search...</div>
  </form>

  <h1 class="abs headline">ENJOY<br>A TRULY MEMORABLE<br>HOLIDAY</h1>
</header>

<section>
  <article class="abs card home">
    <div class="icon"><svg width="40" height="40" viewBox="0 0 40 40"><path d="M5 18 L20 5 L35 18 V35 H5 Z" fill="#fff"/><path d="M12 33 V22 Q20 15 28 22 V33 Z" fill="var(--red)"/></svg></div>
    <div class="photo" role="img" aria-label="Photo of the holiday villa under a blue sky" style="background:linear-gradient(180deg,#4f93df,#a9cdef 35%,#e0cca0 60%,#6d8a4a)"></div>
    <div class="tag">THE HOME</div>
    <div class="more" style="background:var(--red)">read more...</div>
  </article>
  <article class="abs card area">
    <div class="icon"><svg width="44" height="40" viewBox="0 0 44 40"><path d="M4 20 L16 16 L28 22 L40 18 L36 32 L24 30 L12 34 Z" fill="#fff"/><circle cx="24" cy="12" r="6" fill="#fff"/><path d="M19 14 L24 24 L29 14 Z" fill="#fff"/><circle cx="24" cy="12" r="2.5" fill="var(--green)"/></svg></div>
    <div class="photo" role="img" aria-label="Photo of a child on the sand by the shallow sea" style="background:linear-gradient(180deg,#9fc6c9,#c9bfae 50%,#b99f84)"></div>
    <div class="tag">LOCAL AREA</div>
    <div class="more" style="background:var(--green)">read more...</div>
  </article>
  <article class="abs card reviews">
    <div class="icon"><svg width="56" height="48" viewBox="0 0 56 48"><ellipse cx="28" cy="22" rx="26" ry="20" fill="#fff"/><path d="M22 38 L20 47 L30 40 Z" fill="#fff"/><path d="M18 22 H23 V33 H18 Z M25 22 L29 12 Q32 12 31 19 H37 Q39 20 38 23 L36 32 Q35 33 33 33 H25 Z" fill="var(--yellow)"/></svg></div>
    <div class="photo" role="img" aria-label="Photo of a family walking on the beach at sunset" style="background:linear-gradient(180deg,#f3a32a,#e67a14 55%,#6b3a12)"></div>
    <div class="tag">TESTIMONIALS</div>
    <div class="more" style="background:var(--yellow-deep)">read more...</div>
  </article>
  <article class="abs card sights">
    <div class="icon"><svg width="46" height="46" viewBox="0 0 46 46"><path d="M23 2 L27 18 L44 17 L30 26 L36 43 L23 32 L10 43 L16 26 L2 17 L19 18 Z" fill="#fff"/></svg></div>
    <div class="photo" role="img" aria-label="Photo of clownfish among purple sea anemones" style="background:linear-gradient(180deg,#6b4f9e,#9a79c7 50%,#e58a3a 70%,#5a3f86)"></div>
    <div class="tag">TOP ATTRACTIONS</div>
    <div class="more" style="background:var(--blue)">read more...</div>
  </article>
</section>

<section class="abs videos">
  <div class="abs sec-head" style="top:20px">
    <svg width="34" height="24" viewBox="0 0 34 24"><rect x="1" y="6" width="20" height="14" rx="3" fill="none" stroke="#fff" stroke-width="2"/><path d="M21 11 L28 7 V19 L21 15 Z" fill="#fff"/><circle cx="27" cy="6" r="5" fill="#fff"/></svg>
    <span class="pill">OUR VIDEOS</span><span class="rule"></span>
  </div>
  <div class="abs main-video" role="img" aria-label="Video still of a palm-fringed beach with turquoise water">
    <div class="abs play"></div>
  </div>
  <div class="abs clip active" style="top:54px">
    <div class="thumb" role="img" aria-label="Beach video thumbnail"></div>
    <p><b>Lorem ipsum dolor</b><br>&nbsp;sit amet, consectetuer adipiscing elit. Donec ut purus. Suspendisse venenatis. Quisque</p>
  </div>
  <div class="abs clip" style="top:135px">
    <div class="thumb" role="img" aria-label="Beach video thumbnail"></div>
    <p><b>Lorem ipsum dolor</b><br>sit amet, consectetuer adipiscing elit. Donec ut purus. Suspendisse venenatis. Quisque</p>
  </div>
  <div class="abs clip" style="top:206px">
    <div class="thumb" role="img" aria-label="Beach video thumbnail"></div>
    <p><b>Lorem ipsum dolor</b><br>sit amet, consectetuer adipiscing elit. Donec ut purus. Suspendisse venenatis. Quisque</p>
  </div>
</section>

<section class="gallery">
  <div class="abs sec-head" style="top:887px">
    <svg width="36" height="24" viewBox="0 0 36 24"><rect x="1" y="4" width="34" height="19" rx="3" fill="var(--yellow)"/><rect x="5" y="1" width="8" height="4" fill="var(--yellow)"/><circle cx="22" cy="13" r="6" fill="none" stroke="#fff" stroke-width="2"/></svg>
    <span class="pill">GALLERY</span><span class="rule"></span>
  </div>
  <div class="abs shot villa" style="left:57px;top:924px" role="img" aria-label="Villa exterior photo"></div>
  <div class="abs shot beach" style="left:156px;top:924px" role="img" aria-label="Beach photo"></div>
  <div class="abs shot beach" style="left:255px;top:924px" role="img" aria-label="Beach photo"></div>
  <div class="abs shot villa" style="left:354px;top:924px" role="img" aria-label="Villa exterior photo"></div>
  <div class="abs shot beach" style="left:453px;top:924px" role="img" aria-label="Beach photo"></div>
  <div class="abs shot beach" style="left:551px;top:924px" role="img" aria-label="Beach photo"></div>
  <div class="abs shot beach" style="left:57px;top:1026px" role="img" aria-label="Beach photo"></div>
  <div class="abs shot villa" style="left:156px;top:1026px" role="img" aria-label="Villa exterior photo"></div>
  <div class="abs shot beach" style="left:255px;top:1026px" role="img" aria-label="Beach photo"></div>
  <div class="abs shot beach" style="left:354px;top:1026px" role="img" aria-label="Beach photo"></div>
  <div class="abs shot villa" style="left:453px;top:1026px" role="img" aria-label="Villa exterior photo"></div>
  <div class="abs shot beach" style="left:551px;top:1026px" role="img" aria-label="Beach photo"></div>
</section>

<footer class="abs footer">
  Lorem ipsum dolor sit amet, consectetuer adipiscing elit. Aliquam sed erat. Sed non ipsum. Vestibulum ante ipsum primis in faucibus orci luctus et ultrices posuere cubilia Curae; Suspendisse potenti. Nulla sagittis condimentum ligula. Suspendisse viverra placerat tortor. Pellentesque suscipit
</footer>

</body>
</html>
```